Car rental website design for a UAE car rental company

This project is about creating a new website design for a car rental company located in Dubai (United Arab Emirates), I opened the same project a few months ago but I didn't receive a lot of appealing entries so I closed it but this time I am marking the project as guaranteed to avoid such situation again, if you have already provided a design before then please re-submit again on this project so that it is considered while reviewing all the designs

A few important things:

1- We need a simple non-complex design
2- The final deliverable would be 2 screens (PSD, JPEG ... etc), the first screen is for the home page and the second screen is for an internal page
3- The home page must have a section that end users can use to rent a car online directly from the home page instead of going into some inner pages
4- The current website is very old and not very appealing so avoid creating a similar design (www.quarvin-drive.example)
5- The name is Quarvin but the company rents normal cars (no Limousin cars will be rented) so avoid adding any fancy cars in the images/graphics used in the design, just normal end users cars
6- The expected pages would be: home, About us, Our team, Strategy, Contact us and links to social media pages
7- The attachments include the company's logo and some screens from other car rental companies that provide online rentals/payments

If you have any questions please feel free to ask and please note that we will need the designs urgently

Thanks

Target Market(s)

Dubai - United Arab Emirates

Industry/Entity Type

It Company

Number of Pages Required

2 page

Font styles to use
Sans Serif

Requirements
Must have
• Check the project details
Nice to have
Should not have

```html
<!DOCTYPE html>
<html lang="en">
<head>
<meta charset="utf-8">
<title>Quarvin Rent A Car – Home</title>
<link rel="stylesheet" href="https://fonts.googleapis.com/css2?family=Questrial&family=Arimo:wght@400;700&family=Oswald:wght@400;500;700&display=swap">
<style>
:root{
  --crimson:#a3063d;
  --crimson-dark:#8e0434;
  --grey:#7d8886;
  --grey-tab:#8d9c98;
  --ink:#2b2b2b;
  --text:#444;
  --line:#c9c9c9;
  --paper:#ffffff;
  --stage:#e6e6e6;
}
*{box-sizing:border-box;margin:0;padding:0}
html,body{width:1200px;height:927px;overflow:hidden}
body{background:var(--stage);font-family:"Arimo",Arial,sans-serif;color:var(--text)}
.page{position:absolute;left:305px;top:4px;width:590px;height:919px;background:var(--paper);overflow:hidden;box-shadow:0 2px 10px rgba(0,0,0,.12)}
.abs{position:absolute}

/* header */
.brand{left:52px;top:16px;display:flex;flex-direction:column;align-items:center}
.brand-mark{width:22px;height:22px;background:var(--crimson)}
.brand-name{font-family:"Questrial",sans-serif;font-size:16px;color:var(--grey);margin-top:4px}
.brand-tag{font-family:"Arimo",sans-serif;font-size:7px;letter-spacing:1px;color:var(--crimson)}
.support{right:20px;top:16px;display:flex;align-items:center;gap:8px;font-family:"Oswald",sans-serif;font-size:9px;color:var(--ink)}
.support .num{font-size:10px}
.social{right:20px;top:38px;display:flex;gap:14px}
.social span{width:25px;height:25px;border-radius:50%;background:#4a4a4a}

/* navigation */
.nav{left:0;top:77px;width:590px;height:29px;border-top:1px solid var(--crimson);border-bottom:1px solid var(--crimson);display:flex;align-items:center;padding:0 23px}
.nav a{flex:1;text-align:center;font-size:7px;color:var(--ink);text-decoration:none;text-transform:uppercase;border-right:1px solid var(--line);line-height:16px}
.nav a:last-child{border-right:0}
.nav a.active{flex:0 0 56px;margin:0 20px 0 26px;background:var(--crimson);color:#fff;border:0}

/* hero */
.hero-title{left:65px;top:140px;font-family:"Questrial",sans-serif;font-weight:400;font-size:30px;color:var(--crimson);white-space:nowrap}
.hero-title .name{color:var(--grey)}
.hero-rule{left:65px;top:178px;width:270px;height:1px;background:#e0e0e0}
.hero-lead{left:65px;top:185px;width:252px;font-size:8.5px;line-height:12px;color:var(--crimson)}
.hero-copy{left:65px;top:224px;width:252px;font-size:6.5px;line-height:10px;color:var(--ink)}
.arrows{left:65px;top:292px;display:flex;gap:5px}
.arrows span{width:14px;height:14px;border:1px solid var(--crimson);display:flex;align-items:center;justify-content:center}
.hero-car{left:332px;top:186px;width:205px;height:108px;border-radius:40px 60px 20px 20px;background:linear-gradient(180deg,#d9dcde,#9ea4a8)}
.dots{left:278px;top:290px;display:flex;gap:4px}
.dots span{width:5px;height:5px;border-radius:50%;background:#555}
.dots span:first-child{background:#fff;border:1px solid var(--crimson)}

/* section headings */
.sect-title{font-family:"Oswald",sans-serif;font-size:14px;color:var(--crimson);left:40px}
.sect-title.dark{color:var(--ink)}
.sect-rule{left:40px;width:510px;height:1px;background:var(--crimson)}

/* promo */
.promo-car{left:122px;top:392px;width:145px;height:51px;border-radius:30px 40px 12px 12px;background:linear-gradient(180deg,#e0e2e4,#a5abaf)}
.promo-title{left:40px;top:456px;width:310px;text-align:center;font-family:"Oswald",sans-serif;font-weight:700;font-size:20px;letter-spacing:1px;color:var(--ink)}
.promo-title u{text-underline-offset:3px}
.promo-sub{left:40px;top:492px;width:310px;text-align:center;font-family:"Oswald",sans-serif;font-size:9px;color:var(--grey)}
.promo-sub b{color:var(--crimson);font-weight:500}
.btn{background:var(--crimson);color:#fff;font-family:"Oswald",sans-serif;font-size:7px;text-transform:uppercase;display:flex;align-items:center;justify-content:center}
.promo-btn{left:137px;top:515px;width:108px;height:19px}

/* booking */
.booking{left:376px;top:348px;width:174px;font-size:7px;color:var(--crimson)}
.tabs{display:flex;height:15px;border-bottom:1px solid var(--crimson)}
.tab{display:flex;align-items:center;justify-content:center;font-family:"Oswald",sans-serif;font-size:6.5px;color:#fff}
.tab.book{width:56px;background:var(--crimson)}
.tab.manage{flex:1;background:var(--grey-tab)}
.booking .row{position:absolute;left:4px;display:flex;align-items:center;gap:4px;white-space:nowrap}
.field{height:11px;border:1px solid #bbb;font-size:5.5px;color:#555;padding-left:3px;display:flex;align-items:center;background:#fff}
.spin{display:flex;align-items:center;gap:2px}
.spin .box{width:16px}
.spin i{width:8px;height:11px;background:var(--crimson);display:block}
.booking .heading{color:var(--ink);font-size:7.5px}
.opt{font-size:6px;display:flex;align-items:center;gap:3px}
.radio{width:6px;height:6px;border-radius:50%;border:1px solid #aaa}
.check{width:6px;height:6px;border:1px solid #888}
.quote{width:37px;height:10px;font-size:6px;text-transform:none}

/* mission */
.mission-copy{left:55px;top:596px;width:292px;font-size:6.3px;line-height:9.6px;color:var(--ink);text-align:justify}
.mission-btn{left:53px;top:697px;width:63px;height:16px;font-size:6px}
.mission-img{left:375px;top:597px;width:175px;height:114px;background:linear-gradient(135deg,#7fd3d6 0%,#c8d0d0 35%,#8c8c8c 100%);border:1px solid #ddd}

/* service */
.service{left:0;top:726px;width:590px;height:176px;background:var(--crimson);color:#fff}
.service h2{position:absolute;left:42px;top:8px;font-family:"Oswald",sans-serif;font-weight:400;font-size:14px}
.service .intro{position:absolute;left:58px;top:39px;width:480px;font-size:8px;line-height:14px}
.service ul{position:absolute;list-style:none;font-size:6.3px;line-height:14px}
.service ul.left{left:78px;top:70px}
.service ul.right{left:389px;top:70px}
.service li{display:flex;align-items:center;gap:5px}
.service li svg{flex:none}
.service ul.sub{position:static;padding-left:13px;line-height:11.2px;font-size:5.6px}
.service ul.sub li::before{content:"–";margin-right:3px}

/* footer nav */
.foot-nav{left:0;top:902px;width:590px;height:17px;display:flex;align-items:center;padding:0 23px}
.foot-nav a{flex:1;text-align:center;font-size:6.5px;color:var(--ink);text-decoration:none;text-transform:uppercase}
</style>
</head>
<body>
<main class="page">

  <header>
    <div class="abs brand">
      <span class="brand-mark"></span>
      <span class="brand-name">Quarvin</span>
      <span class="brand-tag">Rent A Car</span>
    </div>
    <div class="abs support">
      <span>PHONE SUPPORT</span>
      <svg width="13" height="13" viewBox="0 0 24 24"><path d="M6.6 10.8a15 15 0 0 0 6.6 6.6l2.2-2.2c.3-.3.7-.4 1-.2 1.1.4 2.3.6 3.6.6.6 0 1 .4 1 1V20c0 .6-.4 1-1 1A17 17 0 0 1 3 4c0-.6.4-1 1-1h3.5c.6 0 1 .4 1 1 0 1.3.2 2.5.6 3.6.1.3 0 .7-.2 1z" fill="none" stroke="#a3063d" stroke-width="1.8"/></svg>
      <span class="num">+971 4000 1234</span>
    </div>
    <div class="abs social" aria-label="Social media links"><span></span><span></span><span></span><span></span></div>
  </header>

  <nav class="abs nav">
    <a class="active" href="#">Home</a><a href="#">About us</a><a href="#">Our team</a><a href="#">Strategy</a><a href="#">Contact us</a><a href="#">Gallery</a>
  </nav>

  <section class="hero">
    <h1 class="abs hero-title">Welcome To <span class="name">Quarvin</span></h1>
    <div class="abs hero-rule"></div>
    <p class="abs hero-lead">As Dubai is expected to welcome millions of tourists and visitors, car rental industry is believed to escalate more rapidly in the region.</p>
    <p class="abs hero-copy">Lorem dolor diam et. Clita iusto adipiscing diam sea ipsum. Sanctus diam aliquyam stet vero magna ea. Eos sit consequat ut in invidunt et stet. Vulputate nostrud ea iriure est. Lorem suscipit elit consectetuer erat nisl est sanctus veniam aliquyam. No duis invidunt. Amet odio. Diam illum.</p>
    <div class="abs arrows">
      <span><svg width="6" height="8" viewBox="0 0 6 8"><path d="M5 1 2 4l3 3" fill="none" stroke="#a3063d" stroke-width="1.3"/></svg></span>
      <span><svg width="6" height="8" viewBox="0 0 6 8"><path d="M1 1l3 3-3 3" fill="none" stroke="#a3063d" stroke-width="1.3"/></svg></span>
    </div>
    <div class="abs hero-car" role="img" aria-label="Photo of a silver family sedan"></div>
    <div class="abs dots"><span></span><span></span><span></span></div>
  </section>

  <h2 class="abs sect-title" style="top:317px">Gallary</h2>
  <div class="abs sect-rule" style="top:340px"></div>

  <section class="promo">
    <div class="abs promo-car" role="img" aria-label="Photo of a silver hatchback"></div>
    <h3 class="abs promo-title">EXPERIENCE AN <u>EXTRA</u> MILE</h3>
    <p class="abs promo-sub">of <b>comfort</b>, <b>pleasure</b> and <b>leisure</b> from the best</p>
    <a class="abs btn promo-btn">Read more</a>
  </section>

  <form class="abs booking">
    <div class="tabs"><span class="tab book">Book a Car</span><span class="tab manage">View,modify or cancel a booking</span></div>
    <div class="row" style="top:24px">Rental Start Date/Time</div>
    <div class="row" style="top:37px"><span class="field" style="width:82px">27 March 2015</span><span class="spin" style="margin-left:6px"><span class="field box">10</span><i></i></span><span class="spin"><span class="field box">00</span><i></i></span></div>
    <div class="row" style="top:55px">Rental End Date/Time</div>
    <div class="row" style="top:66px"><span class="field" style="width:82px">27 March 2015</span><span class="spin" style="margin-left:6px"><span class="field box">10</span><i></i></span><span class="spin"><span class="field box">00</span><i></i></span></div>
    <div class="row" style="top:83px;left:auto;right:4px">Number of Days 2</div>
    <div class="row heading" style="top:106px">Pick-up Location(City, State or Airport Code)</div>
    <div class="row" style="top:119px;gap:30px"><span class="opt"><span class="radio"></span>Choose Station</span><span class="opt"><span class="radio"></span>Choose Car Type</span></div>
    <div class="row" style="top:134px"><span class="opt"><span class="check"></span>Returning to Same as pickup location</span></div>
    <div class="row" style="top:149px"><span style="width:72px">Pickup rental country</span><span class="field" style="width:70px">Dubai</span><i style="width:9px;height:11px;background:var(--crimson);display:block"></i></div>
    <div class="row" style="top:168px"><span style="width:72px">Rental location</span><span class="field" style="width:79px"></span></div>
    <div class="row" style="top:183px"><span style="width:72px">Sign Up your account</span><span class="field" style="width:70px">Select an account type</span><i style="width:9px;height:11px;background:var(--crimson);display:block"></i></div>
    <div class="row" style="top:203px"><span class="opt" style="font-size:5px"><span class="check"></span>Apply any discount Code</span><span class="btn quote" style="margin-left:26px">Get Quote</span></div>
  </form>

  <h2 class="abs sect-title dark" style="top:567px">Mission &amp; Vision</h2>
  <div class="abs sect-rule" style="top:590px;width:510px"></div>

  <section>
    <p class="abs mission-copy">No sit feugiat consetetur volutpat et. Iriure magna ut at eirmod vero odio blandit sea gubergren lorem. Labore ea eu lorem sed labore feugiat feugiat ullamcorper. Dolor no ut augue rebum sanctus esse illum sadipscing exerci. Sanctus placerat eirmod ut amet sit et lorem.<br>No sit feugiat consetetur volutpat et. Iriure magna ut at eirmod vero odio blandit sea gubergren lorem. Labore ea eu lorem sed labore feugiat feugiat ullamcorper. Dolor no ut augue rebum sanctus esse illum sadipscing exerci. Sanctus placerat eirmod ut amet sit et lorem.</p>
    <a class="abs btn mission-btn">Read more</a>
    <div class="abs mission-img" role="img" aria-label="Photo of a hand holding a car key"></div>
  </section>

  <section class="abs service">
    <h2>Service</h2>
    <p class="intro">Quarvin offers a comprehensive range of services including daily, short term and long term rental, chauffeur drive services for every purpose and budget.</p>
    <ul class="left">
      <li><svg width="7" height="7" viewBox="0 0 8 8"><circle cx="4" cy="4" r="3.3" fill="none" stroke="#fff" stroke-width=".8"/><path d="M2.4 4l1.1 1.1L5.7 2.9" fill="none" stroke="#fff" stroke-width=".8"/></svg>Wide range of vehicles for city driving or SUV's for trips</li>
      <li><svg width="7" height="7" viewBox="0 0 8 8"><circle cx="4" cy="4" r="3.3" fill="none" stroke="#fff" stroke-width=".8"/><path d="M2.4 4l1.1 1.1L5.7 2.9" fill="none" stroke="#fff" stroke-width=".8"/></svg>Special 10% discount for new customers on the first rent</li>
      <li><svg width="7" height="7" viewBox="0 0 8 8"><circle cx="4" cy="4" r="3.3" fill="none" stroke="#fff" stroke-width=".8"/><path d="M2.4 4l1.1 1.1L5.7 2.9" fill="none" stroke="#fff" stroke-width=".8"/></svg>Long term car rental</li>
      <li><ul class="sub">
        <li>New vehicles</li>
        <li>Fixed monthly expenditure</li>
        <li>Free registration and insurance</li>
        <li>Free maintenance and replacement vehicles</li>
        <li>No finance costs and no hidden costs</li>
      </ul></li>
    </ul>
    <ul class="right">
      <li><svg width="7" height="7" viewBox="0 0 8 8"><circle cx="4" cy="4" r="3.3" fill="none" stroke="#fff" stroke-width=".8"/><path d="M2.4 4l1.1 1.1L5.7 2.9" fill="none" stroke="#fff" stroke-width=".8"/></svg>Sightseeing tours</li>
      <li><svg width="7" height="7" viewBox="0 0 8 8"><circle cx="4" cy="4" r="3.3" fill="none" stroke="#fff" stroke-width=".8"/><path d="M2.4 4l1.1 1.1L5.7 2.9" fill="none" stroke="#fff" stroke-width=".8"/></svg>Buyback option after lease term</li>
      <li><svg width="7" height="7" viewBox="0 0 8 8"><circle cx="4" cy="4" r="3.3" fill="none" stroke="#fff" stroke-width=".8"/><path d="M2.4 4l1.1 1.1L5.7 2.9" fill="none" stroke="#fff" stroke-width=".8"/></svg>Special offers for online bookings</li>
      <li><svg width="7" height="7" viewBox="0 0 8 8"><circle cx="4" cy="4" r="3.3" fill="none" stroke="#fff" stroke-width=".8"/><path d="M2.4 4l1.1 1.1L5.7 2.9" fill="none" stroke="#fff" stroke-width=".8"/></svg>Airport transfers</li>
    </ul>
  </section>

  <footer class="abs foot-nav">
    <a href="#">Home</a><a href="#">About us</a><a href="#">Our team</a><a href="#">Strategy</a><a href="#">Contact us</a><a href="#">Gallery</a>
  </footer>

</main>
</body>
</html>
```